Business Card Design

Certified GKL Instructor. Self defense instruction. Ladies classes available. Semi automatic and revolver

Industry/Entity Type

Defense

```html
<!DOCTYPE html>
<html lang="en">
<head>
<meta charset="utf-8">
<title>Dana Whitfield – Business Card</title>
<link rel="stylesheet" href="https://fonts.googleapis.com/css2?family=PT+Sans&family=PT+Serif&display=swap">
<style>
  :root {
    --page-bg: #2a2a2a;
    --card-bg: #ffffff;
    --navy: #2b2f7a;
    --grey: #6f6f6f;
    --tick-red: #e0203a;
    --blue-deep: #1668c4;
    --blue-mid: #1fa3e6;
    --blue-light: #bfe6f8;
    --badge-navy: #2e3276;
  }
  * { box-sizing: border-box; margin: 0; padding: 0; }
  html, body {
    width: 1200px; height: 942px; overflow: hidden;
    background: var(--page-bg);
  }
  .card {
    position: absolute; left: 50px; top: 168px;
    width: 1100px; height: 606px;
    background: var(--card-bg);
    overflow: hidden;
  }
  .card__pattern {
    position: absolute; inset: 0;
    background:
      linear-gradient(62deg, var(--blue-deep) 0%, var(--blue-mid) 30%, var(--blue-light) 45%, rgba(255,255,255,0) 58%),
      linear-gradient(180deg, rgba(255,255,255,0) 60%, rgba(191,230,248,0.5) 100%);
  }
  .badge {
    position: absolute; left: 133px; top: 73px;
    width: 196px; height: 196px; border-radius: 50%;
    background: var(--badge-navy);
    border: 6px solid #ffffff;
    box-shadow: 0 0 0 2px var(--badge-navy);
  }
  .scene-illustration {
    position: absolute; left: 62px; top: 278px;
    width: 343px; height: 267px;
    background: linear-gradient(90deg, rgba(20,50,80,0.75), rgba(30,60,90,0.7) 60%, rgba(170,70,60,0.75));
    border-radius: 40px 40px 8px 8px;
  }
  .identity {
    position: absolute; right: 158px; top: 84px; text-align: right;
    font-family: "PT Serif", serif;
  }
  .identity__name { font-size: 62px; color: var(--navy); line-height: 1; }
  .identity__role { font-size: 31px; color: var(--grey); line-height: 1.2; margin-top: 2px; }
  .services {
    position: absolute; left: 453px; top: 222px;
    list-style: none;
    font-family: "PT Sans", sans-serif; font-size: 34px; color: var(--navy);
  }
  .services li { height: 48px; display: flex; align-items: center; }
  .services svg { width: 44px; height: 34px; margin-right: 13px; flex: none; }
  .contact {
    position: absolute; left: 453px; top: 412px;
    font-family: "PT Serif", serif; font-size: 34px; color: var(--navy);
  }
  .contact__row { display: flex; align-items: center; height: 64px; }
  .contact__icon {
    width: 40px; height: 40px; border-radius: 50%;
    background: var(--navy); margin-right: 17px; flex: none;
    display: flex; align-items: center; justify-content: center;
  }
</style>
</head>
<body>
  <div class="card">
    <div class="card__pattern"></div>
    <div class="badge" role="img" aria-label="Certification badge"></div>
    <div class="scene-illustration" role="img" aria-label="Silhouettes of two pairs practising self defense moves"></div>

    <div class="identity">
      <div class="identity__name">Dana Whitfield</div>
      <div class="identity__role">instruction</div>
    </div>

    <ul class="services">
      <li><svg viewBox="0 0 44 34"><path d="M2 20 L9 15 L16 24 L38 2 L42 6 L16 33 Z" fill="var(--tick-red)"/></svg>Self defense instruction.</li>
      <li><svg viewBox="0 0 44 34"><path d="M2 20 L9 15 L16 24 L38 2 L42 6 L16 33 Z" fill="var(--tick-red)"/></svg>Ladies classes available.</li>
      <li><svg viewBox="0 0 44 34"><path d="M2 20 L9 15 L16 24 L38 2 L42 6 L16 33 Z" fill="var(--tick-red)"/></svg>Semi automatic and revolver</li>
    </ul>

    <div class="contact">
      <div class="contact__row">
        <span class="contact__icon">
          <svg width="24" height="18" viewBox="0 0 24 18"><rect x="1" y="1" width="22" height="16" rx="2" fill="none" stroke="#fff" stroke-width="2"/><path d="M1 2 L12 10 L23 2 M1 16 L9 8 M23 16 L15 8" fill="none" stroke="#fff" stroke-width="1.6"/></svg>
        </span>
        whitfieldda@mailbox.com
      </div>
      <div class="contact__row">
        <span class="contact__icon">
          <svg width="22" height="22" viewBox="0 0 24 24"><path d="M6.6 10.8a15.1 15.1 0 0 0 6.6 6.6l2.2-2.2a1 1 0 0 1 1-.25 11.4 11.4 0 0 0 3.6.57 1 1 0 0 1 1 1V20a1 1 0 0 1-1 1A17 17 0 0 1 3 4a1 1 0 0 1 1-1h3.5a1 1 0 0 1 1 1c0 1.25.2 2.45.57 3.57a1 1 0 0 1-.25 1z" fill="#fff"/></svg>
        </span>
        555-014-2290
      </div>
    </div>
  </div>
</body>
</html>
```